Design eines privaten Leadership-Leitbildes
Zielgruppe
Es geht um mein privates Leadership-Leitbild. Ich bin CEO eines Unternehmens, das sich in der Schweiz und international intensiv mit der Digitalen Transformation im Bauwesen befasst (www.tlv-bau.ch).
Aufgabenstellung
Die Vorlage ist bereits recht konkret und beinhaltet alles. In der grafischen Aufbereitung ist der Kreative frei. Allerdings geht es um einen Business-Content und bei meinem Leadership-Leitbild um meine persönliche 'Visitenkarte'. Also nicht 'verspielt' oder 'witzig'. Das Plakat soll A4 und A3 genutzt werden und auch auf einem gängigen Laser-Drucker in guter Qualität ausgedruckt werden können.

```html
<!DOCTYPE html>
<html lang="de">
<head>
<meta charset="utf-8">
<title>Leadership-Leitbild</title>
<link rel="stylesheet" href="https://fonts.googleapis.com/css2?family=Bebas+Neue&family=Open+Sans:wght@400;700&display=swap">
<style>
  :root {
    --bg: #4a4b4d;
    --bg-light: #55565a;
    --bg-dark: #434446;
    --accent: #d4792a;
    --text: #f3f3f3;
  }
  * { margin: 0; padding: 0; box-sizing: border-box; }
  html, body { width: 848px; height: 1200px; overflow: hidden; background: var(--bg); }
  .poster {
    position: relative;
    width: 848px;
    height: 1200px;
    background: var(--bg);
    color: var(--text);
    font-family: "Open Sans", Arial, sans-serif;
    overflow: hidden;
  }
  .skyline {
    position: absolute;
    left: 0;
    top: 230px;
    width: 848px;
    height: 970px;
    background:
      radial-gradient(ellipse 55% 60% at 62% 40%, var(--bg-light) 0%, rgba(85,86,90,0) 70%),
      linear-gradient(180deg, rgba(67,68,70,0) 0%, var(--bg-dark) 100%);
  }
  .brand {
    position: absolute;
    left: 427px;
    top: 0;
    width: 400px;
    height: 70px;
  }
  .brand-name {
    position: absolute;
    left: 0;
    top: 4px;
    font-weight: 700;
    font-size: 56px;
    line-height: 1;
    letter-spacing: 6px;
    color: var(--text);
  }
  .brand-tagline {
    position: absolute;
    left: 210px;
    top: 53px;
    font-weight: 400;
    font-size: 12.5px;
    letter-spacing: 0.4px;
    color: var(--text);
    white-space: nowrap;
  }
  .section {
    position: absolute;
    left: 72px;
    width: 740px;
  }
  .kicker {
    font-family: "Bebas Neue", Impact, sans-serif;
    font-weight: 400;
    font-size: 34px;
    line-height: 28px;
    color: var(--text);
  }
  .title {
    font-family: "Bebas Neue", Impact, sans-serif;
    font-weight: 400;
    font-size: 64px;
    line-height: 56px;
    color: var(--accent);
    margin-top: 2px;
  }
  .body {
    font-weight: 700;
    font-size: 18.4px;
    line-height: 23.3px;
    text-transform: uppercase;
    white-space: nowrap;
  }
  .statement .body { margin-top: -3px; }
  .mission .body, .values .body, .vision .body { margin-top: 9px; }
  .vision p + p { margin-top: 23.3px; }
  .statement { top: 77px; }
  .mission { top: 209px; }
  .values { top: 371px; }
  .vision { top: 560px; }
</style>
</head>
<body>
<main class="poster">
  <div class="skyline" role="img" aria-label="Dezente Stadtsilhouette aus Gebäuden mit Fensterrastern im Hintergrund"></div>

  <header class="brand">
    <span class="brand-name">TLV</span>
    <span class="brand-tagline">Digitale Praxis im Bau</span>
  </header>

  <section class="section statement">
    <h2 class="kicker">Mein</h2>
    <h1 class="title">ID-Statement</h1>
    <p class="body">Ich bin der klare Laser Richtung Freiheit!</p>
  </section>

  <section class="section mission">
    <h2 class="kicker">Meine</h2>
    <h2 class="title">Mission</h2>
    <p class="body">Ich fördere Menschen, die mir vertrauen, um gemeinsam Wunder<br>geschehen zu lassen, die uns im Herzen verbinden.</p>
  </section>

  <section class="section values">
    <h2 class="kicker">Meine</h2>
    <h2 class="title">Werte</h2>
    <p class="body">Authentizität, Integrität, Gestalten, Begeisterung, Verantwortung,<br>Menschlichkeit, Empathie, Klarheit, Transparenz, Weisheit, Weit-<br>blick, Erfolg</p>
  </section>

  <section class="section vision">
    <h2 class="kicker">Meine</h2>
    <h2 class="title">Vision</h2>
    <div class="body">
      <p>Ich vertraue den Mitarbeitenden und bin offen. Offenheit meint<br>dabei sowohl den offenen Umgang mit Informationen, als auch<br>auf die Offenheit für Neues und die Freude am Experimentieren.</p>
      <p>Ich begegne allen Mitarbeitenden auf Augenhöhe. Visionen und<br>Ziele werden gemeinsam entwickelt. Es zählen die besten Argu-<br>mente und Ideen, keine anderen Faktoren wie Position, Alter, Ges-<br>chlecht oder Herkunft.</p>
      <p>Ich begleite und fördere meine Mitarbeitenden. Dazu schaffe ich die<br>notwendigen Räume und Möglichkeiten: Ich gestalte damit den<br>Rahmen und die Struktur für höchste «Performance», und lasse<br>den Mitarbeitenden maximalen Gestaltungsspielraum.</p>
      <p>Ich fördere und fordere in meiner Organisation Schnelligkeit,<br>Agilität und Flexibilität.</p>
      <p>Ich sorge dafür, dass uns in allen Aktivitäten stets das weltweit<br>bestmögliche Wissen zur Verfügung steht und baue dafür auf aktiv<br>gelebte Partnerschaften.</p>
    </div>
  </section>
</main>
</body>
</html>
```